Business Card Design for Irrigation Contractor

Design and layout for company business cards to include the following information:
1. Logo
2. Installation \ Service \ Maintenance
3. U-47283
4. Walter J. Lindqvist
5. walter@7Kirrigation.com
6. Office 555-712-9364
7. Cell 555-286-0517

```html
<!DOCTYPE html>
<html lang="en">
<head>
<meta charset="utf-8">
<title>7K Irrigation – Business Card</title>
<link rel="stylesheet" href="https://fonts.googleapis.com/css2?family=Montserrat:wght@600;800&family=Raleway:wght@500;700&display=swap">
<style>
  :root {
    --page-bg: #ebe8e3;
    --card-white: #f7f8f9;
    --navy: #1b4f7f;
    --navy-deep: #17436d;
    --band-blue: #1a5488;
    --back-blue-a: #1a548c;
    --back-blue-b: #1f66a6;
    --icon-blue: #4aa6dc;
    --text-dark: #1e1e22;
    --light-grey: #e4e6e9;
    --wave-grey: #e3e5e8;
  }
  * { box-sizing: border-box; margin: 0; padding: 0; }
  html, body { width: 900px; height: 1200px; overflow: hidden; }
  body { background: var(--page-bg); position: relative; font-family: "Raleway", sans-serif; }

  .card { position: absolute; border-radius: 24px; overflow: hidden; box-shadow: 0 6px 18px rgba(0,0,0,.12); }

  /* Front */
  .card-front { left: 72px; top: 135px; width: 773px; height: 448px; background: var(--card-white); }
  .wave-pattern { position: absolute; left: 0; top: 0; width: 100%; height: 110px;
    background: linear-gradient(180deg, var(--wave-grey) 0%, rgba(247,248,249,0) 100%); }
  .brand-mark { position: absolute; left: 150px; top: 130px; width: 100px; height: 100px; border-radius: 50%; background: var(--icon-blue); }
  .brand-name { position: absolute; left: 0; width: 400px; top: 258px; text-align: center;
    font-family: "Montserrat", sans-serif; font-weight: 800; font-size: 37px; color: var(--navy-deep); letter-spacing: -0.5px; }
  .license { position: absolute; left: 0; width: 400px; top: 302px; text-align: center;
    font-family: "Montserrat", sans-serif; font-weight: 600; font-size: 20px; color: var(--navy-deep); letter-spacing: 1px; }
  .person-name { position: absolute; left: 406px; top: 120px; font-weight: 700; font-size: 31px; color: var(--navy); }
  .contact-list { position: absolute; left: 406px; top: 190px; list-style: none; }
  .contact-item { display: flex; align-items: center; height: 36px; margin-bottom: 14px; font-family: "Raleway", sans-serif; font-weight: 500; font-size: 23px; color: var(--text-dark); }
  .contact-icon { width: 36px; height: 36px; border-radius: 50%; background: var(--icon-blue); margin-right: 12px; display: flex; align-items: center; justify-content: center; }
  .services-band { position: absolute; left: 0; bottom: 0; width: 100%; height: 78px; background: var(--band-blue);
    display: flex; align-items: center; justify-content: center; gap: 34px;
    font-family: "Montserrat", sans-serif; font-weight: 600; font-size: 22px; letter-spacing: 2px; color: #fff; }

  /* Back */
  .card-back { left: 74px; top: 625px; width: 774px; height: 447px;
    background: linear-gradient(90deg, var(--back-blue-a) 0%, var(--back-blue-b) 100%); }
  .back-mark { position: absolute; left: 288px; top: 75px; width: 200px; height: 200px; border-radius: 50%; background: var(--light-grey); }
  .back-name { position: absolute; left: 0; width: 100%; top: 305px; text-align: center;
    font-family: "Montserrat", sans-serif; font-weight: 800; font-size: 76px; color: var(--light-grey); letter-spacing: 0.5px; }
</style>
</head>
<body>

<section class="card card-front">
  <div class="wave-pattern" role="img" aria-label="Fine grey wavy line pattern along the top edge"></div>

  <div class="brand-mark"></div>
  <div class="brand-name">7K IRRIGATION</div>
  <div class="license">U-47283</div>

  <h1 class="person-name">Walter J. Lindqvist</h1>
  <ul class="contact-list">
    <li class="contact-item">
      <span class="contact-icon">
        <svg width="20" height="20" viewBox="0 0 24 24"><path fill="#fff" d="M6.6 10.8a15.1 15.1 0 0 0 6.6 6.6l2.2-2.2c.3-.3.7-.4 1-.2 1.1.4 2.3.6 3.6.6.6 0 1 .4 1 1V20c0 .6-.4 1-1 1A17 17 0 0 1 3 4c0-.6.4-1 1-1h3.5c.6 0 1 .4 1 1 0 1.3.2 2.5.6 3.6.1.3 0 .7-.2 1z"/></svg>
      </span>555-712-9364
    </li>
    <li class="contact-item">
      <span class="contact-icon">
        <svg width="20" height="20" viewBox="0 0 24 24"><rect x="7" y="2" width="10" height="20" rx="2" fill="none" stroke="#fff" stroke-width="2"/><circle cx="12" cy="18" r="1.2" fill="#fff"/></svg>
      </span>555-286-0517
    </li>
    <li class="contact-item">
      <span class="contact-icon">
        <svg width="20" height="20" viewBox="0 0 24 24"><rect x="3" y="6" width="18" height="12" rx="1" fill="none" stroke="#fff" stroke-width="2"/><path d="M3 7l9 6 9-6" fill="none" stroke="#fff" stroke-width="2"/></svg>
      </span>walter@7Kirrigation.com
    </li>
  </ul>

  <div class="services-band">
    <span>Installation</span><span>|</span><span>Service</span><span>|</span><span>Maintenance</span>
  </div>
</section>

<section class="card card-back">
  <div class="back-mark"></div>
  <div class="back-name">7K IRRIGATION</div>
</section>

</body>
</html>
```